Mental Health care Company in Washington DC

We are a new mental health care services provider in Washington DC. Please look at these sites.
https://marlowbrookpartners.com
https://www.quillstoneinc.com
https://velmarsh-kt.org/
https://www.trivanqx.com
https://www.thelanternofqz.com

```html
<!DOCTYPE html>
<html lang="en">
<head>
<meta charset="utf-8">
<title>Novera Health Services – Mental Wellness in Washington DC</title>
<link href="https://fonts.googleapis.com/css2?family=Outfit:wght@300;400;500;600&display=swap" rel="stylesheet">
<style>
:root{
  --navy:#0b1c3d;
  --navy-deep:#071532;
  --orange:#f4a163;
  --teal:#9fd8d9;
  --teal-text:#8fd3d4;
  --mint-bg:#e3f3f3;
  --grey-bg:#f5f5f5;
  --peach-bg:#fdf1e9;
  --text:#3b3f4a;
  --muted:#5a5f6a;
  --white:#ffffff;
}
*{margin:0;padding:0;box-sizing:border-box}
html,body{width:1200px;height:4128px;overflow:hidden}
body{position:relative;font-family:'Outfit',sans-serif;color:var(--text);background:var(--white)}
.abs{position:absolute}
.bg-shapes{position:absolute;left:0;top:0;width:1200px;height:4128px}

/* header */
.logo-badge{left:110px;top:-70px;width:178px;height:174px;background:var(--white);border-radius:50%;display:flex;align-items:flex-end;justify-content:center;padding-bottom:52px;z-index:3}
.brand{font-size:24px;font-weight:500;color:var(--navy);letter-spacing:-.3px}
.nav{left:250px;top:35px;width:840px;height:42px;background:var(--white);border-radius:21px;display:flex;align-items:center;z-index:2}
.nav a{position:absolute;font-size:12.5px;color:var(--navy);text-decoration:none;font-weight:400}
.nav a.active{color:var(--orange)}
.btn-request{right:6px;top:5px;height:32px;padding:0 18px;background:var(--navy);color:var(--white)!important;border-radius:16px;display:flex;align-items:center;font-size:12.5px}

/* hero */
.hero-photo{left:0;top:0;width:1200px;height:566px}
.hero-title{left:110px;top:162px;font-size:34px;font-weight:500;color:var(--white);line-height:53px}
.hero-title span{color:var(--orange)}
.hero-text{left:110px;top:285px;font-size:16px;line-height:37px;color:var(--white);font-weight:300}
.btn-outline{left:110px;top:388px;width:164px;height:42px;border:1.5px solid var(--white);border-radius:21px;color:var(--white);font-size:14px;display:flex;align-items:center;justify-content:center}

/* common */
.btn-orange{background:var(--orange);color:var(--white);border-radius:22px;font-size:14px;display:flex;align-items:center;justify-content:center}
.section-title{font-size:33px;font-weight:500;color:var(--navy);width:1200px;text-align:center;left:0}
.photo{border-radius:50%}

/* about */
.about-photo{left:111px;top:691px;width:486px;height:486px}
.about-title{left:658px;top:642px;font-size:30px;font-weight:500;color:var(--navy)}
.about-text{left:658px;top:704px;width:440px;font-size:15px;line-height:37.6px;color:var(--text)}
.about-text p+p{margin-top:11px}

/* services */
.service-card{width:302px;height:338px;border:2px solid #eeeeee;border-radius:22px;background:var(--white);text-align:center}
.service-card.featured{background:var(--navy);border-color:var(--navy);height:333px;width:298px}
.service-icon{width:80px;height:80px;border-radius:50%;background:var(--navy);margin:42px auto 0;display:flex;align-items:center;justify-content:center}
.featured .service-icon{background:var(--white)}
.service-name{font-size:19px;font-weight:400;color:var(--orange);margin-top:26px}
.featured .service-name{color:var(--teal-text)}
.service-text{font-size:15px;line-height:36.5px;color:var(--muted);margin-top:6px;padding:0 24px}
.featured .service-text{color:var(--white)}

/* communities */
.comm-title{left:110px;top:1936px;font-size:31px;font-weight:500;color:var(--navy);line-height:53px}
.comm-text{left:110px;top:2052px;width:420px;font-size:15px;line-height:37.8px;color:var(--text)}

/* what we do */
.do-card{width:462px;height:212px;background:var(--white);border-radius:6px;box-shadow:0 4px 18px rgba(11,28,61,.05)}
.do-card::before{content:"";position:absolute;left:0;top:80px;width:4px;height:48px;background:var(--teal)}
.do-title{position:absolute;left:38px;top:26px;width:300px;font-size:21px;font-weight:500;color:var(--navy);line-height:38px}
.do-text{position:absolute;left:40px;width:320px;font-size:15px;line-height:36.5px;color:var(--muted)}
.arrow-btn{position:absolute;right:16px;bottom:16px;width:42px;height:42px;border-radius:50%;background:var(--navy);display:flex;align-items:center;justify-content:center}

/* testimonials */
.testimonial{left:304px;top:3468px;width:592px;height:238px;border:2px solid #f1f1f1;border-radius:18px;background:var(--white);text-align:center}
.quote-mark{position:absolute;left:266px;top:-4px;font-size:90px;line-height:90px;color:#e0e0e0;font-family:Georgia,serif}
.testimonial-text{margin-top:58px;font-size:15px;line-height:36.5px;color:var(--muted);padding:0 30px}
.testimonial-name{font-size:17px;color:var(--orange);margin-top:8px}

/* footer */
.footer{left:0;top:3793px;width:1200px;height:335px;background:var(--navy)}
.footer-brand{left:138px;top:3850px;font-size:44px;font-weight:400;color:var(--white);letter-spacing:-.5px}
.footer-sub{left:140px;top:3899px;font-size:15px;letter-spacing:8px;color:var(--white);font-weight:300}
.footer-heading{font-size:25px;font-weight:500;color:var(--orange)}
.footer-link{font-size:13.5px;color:var(--white)}
.copyright{left:138px;top:4082px;font-size:13px;color:var(--white)}
.copyright span{color:var(--orange)}
.social{width:27px;height:27px;border:1.5px solid var(--white);border-radius:50%}
</style>
</head>
<body>

<svg class="bg-shapes" viewBox="0 0 1200 4128" aria-hidden="true">
  <!-- about band -->
  <path d="M0 480 H1200 V1178 C1080 1110 960 1060 760 1090 C560 1120 300 1130 160 1070 C80 1040 30 1020 0 1010 Z" fill="var(--mint-bg)"/>
  <!-- communities band -->
  <path d="M0 1805 C200 1830 380 1870 600 1858 C820 1846 1000 1820 1200 1830 V2460 H0 Z" fill="var(--grey-bg)"/>
  <!-- what we do band -->
  <path d="M0 2490 C160 2470 300 2440 460 2445 C700 2452 900 2500 1200 2470 V3200 C1150 3260 1100 3300 1040 3310 C880 3330 760 3250 600 3260 C400 3272 200 3300 0 3350 Z" fill="var(--peach-bg)"/>
</svg>

<!-- hero -->
<svg class="abs hero-photo" viewBox="0 0 1200 566" role="img" aria-label="Photo of a support group sitting in a circle in a bright room, with a dark navy overlay">
  <defs>
    <linearGradient id="heroGrad" x1="0" y1="0" x2="1" y2="0">
      <stop offset="0" stop-color="#12264f"/>
      <stop offset=".45" stop-color="#2a3a57"/>
      <stop offset="1" stop-color="#6b6a66"/>
    </linearGradient>
  </defs>
  <path d="M0 0 H1200 V540 C1000 575 820 560 600 548 C360 535 160 520 0 512 Z" fill="url(#heroGrad)"/>
</svg>

<div class="abs logo-badge"><span class="brand">Novera Health</span></div>
<nav class="abs nav">
  <a class="active" style="left:102px;top:13px">HOME</a>
  <a style="left:172px;top:13px">ABOUT US</a>
  <a style="left:268px;top:13px">SERVICES</a>
  <a style="left:361px;top:13px">INSURANCE</a>
  <a style="left:464px;top:13px">FAQS</a>
  <a style="left:531px;top:13px">CONTACT</a>
  <a class="btn-request">REQUEST AN APPOINTMENT</a>
</nav>

<h1 class="abs hero-title">Your <span>Mental Wellness</span><br>Begins Here</h1>
<p class="abs hero-text">Compassionate care for every stage of life, right<br>here in Washington DC.</p>
<div class="abs btn-outline">MEET OUR TEAM</div>

<!-- about -->
<div class="abs photo about-photo" role="img" aria-label="Photo of a young woman smiling during a counselling session with a therapist" style="background:radial-gradient(circle at 35% 45%,#e8dccd,#b9a48e 60%,#3e3a36)"></div>
<h2 class="abs about-title">About Novera Health</h2>
<div class="abs about-text">
  <p>At Novera Health, we believe that mental wellness is the foundation of a healthy and fulfilling life. Located in the heart of Washington, DC, our mission is to provide accessible, evidence-based mental health services tailored to the diverse needs of our community.</p>
  <p>Whether you're navigating anxiety, depression, trauma</p>
</div>
<div class="abs btn-orange" style="left:658px;top:974px;width:146px;height:42px">LEARN MORE</div>

<!-- services -->
<h2 class="abs section-title" style="top:1250px">Services We Offer</h2>

<div class="abs service-card" style="left:110px;top:1318px">
  <div class="service-icon">
    <svg width="40" height="40" viewBox="0 0 40 40" fill="none" stroke="#fff" stroke-width="1.6"><path d="M12 32v-6c-4-2-6-6-5-11 1-6 7-9 13-8 6 1 9 6 8 11l3 5h-3v4c0 2-2 3-4 3h-2v2"/><circle cx="19" cy="16" r="4"/></svg>
  </div>
  <div class="service-name">Psychiatric Consultations</div>
  <p class="service-text">Lorem ipsum dolor sit amet, consectetur adipiscing elit, sed do eiusmod tempor incididunt ut</p>
</div>

<div class="abs service-card featured" style="left:450px;top:1354px">
  <div class="service-icon">
    <svg width="40" height="40" viewBox="0 0 40 40" fill="none" stroke="var(--navy)" stroke-width="1.6"><path d="M8 34h24M12 34V20h6v14M22 34V14h6v20M10 14l8-6 6 4 8-6"/></svg>
  </div>
  <div class="service-name">Substance Abuse/Addiction</div>
  <p class="service-text">Lorem ipsum dolor sit amet, consectetur adipiscing elit, sed do eiusmod tempor incididunt ut</p>
</div>

<div class="abs service-card" style="left:787px;top:1318px">
  <div class="service-icon">
    <svg width="40" height="40" viewBox="0 0 40 40" fill="none" stroke="#fff" stroke-width="1.6"><circle cx="20" cy="11" r="4"/><path d="M13 24c0-4 3-7 7-7s7 3 7 7M7 26h26v4H7zM10 30v4M30 30v4"/></svg>
  </div>
  <div class="service-name">Family Counseling &amp; Therapy</div>
  <p class="service-text">Lorem ipsum dolor sit amet, consectetur adipiscing elit, sed do eiusmod tempor incididunt ut</p>
</div>

<div class="abs btn-orange" style="left:497px;top:1732px;width:206px;height:42px">VIEW MORE SERVICES</div>

<!-- communities -->
<h2 class="abs comm-title">Empowering Communities<br>for Better Life</h2>
<p class="abs comm-text">At Novera Health, we are more than a mental health provider — we are a trusted partner in your journey toward healing, growth, and resilience. Rooted in Washington, DC, our mission is to empower individuals and families through accessible, culturally-responsive, and compassionate mental health care.</p>
<div class="abs btn-orange" style="left:110px;top:2310px;width:223px;height:42px">LEARN MORE ABOUT US</div>

<svg class="abs" style="left:580px;top:1850px" width="520" height="540" viewBox="0 0 520 540" aria-hidden="true">
  <circle cx="120" cy="377" r="112" fill="var(--teal)"/>
  <circle cx="285" cy="233" r="224" fill="none" stroke="var(--orange)" stroke-width="3"/>
</svg>
<div class="abs photo" style="left:623px;top:1926px;width:442px;height:442px;background:radial-gradient(circle at 50% 60%,#d9a273,#8e9a5e 55%,#566a3c)" role="img" aria-label="Photo of a diverse group of friends joining hands together outdoors"></div>

<!-- what we do -->
<h2 class="abs section-title" style="top:2532px">What We Do</h2>

<div class="abs do-card" style="left:120px;top:2614px">
  <div class="do-title">Children and Adolescent Services</div>
  <p class="do-text" style="top:112px">Lorem ipsum dolor sit amet, consectetur adipiscing elit, sed do eiusmod</p>
  <div class="arrow-btn"><svg width="16" height="16" viewBox="0 0 16 16" fill="none" stroke="#fff" stroke-width="1.8"><path d="M4 12L12 4M6 4h6v6"/></svg></div>
</div>
<div class="abs do-card" style="left:617px;top:2635px">
  <div class="do-title">Substance Use Intervention Program</div>
  <p class="do-text" style="top:112px">Lorem ipsum dolor sit amet, consectetur adipiscing elit, sed do eiusmod</p>
  <div class="arrow-btn"><svg width="16" height="16" viewBox="0 0 16 16" fill="none" stroke="#fff" stroke-width="1.8"><path d="M4 12L12 4M6 4h6v6"/></svg></div>
</div>
<div class="abs do-card" style="left:120px;top:2861px">
  <div class="do-title">Housing Referrals</div>
  <p class="do-text" style="top:74px">Lorem ipsum dolor sit amet, consectetur adipiscing elit, sed do eiusmod tempor incididunt ut labore</p>
  <div class="arrow-btn"><svg width="16" height="16" viewBox="0 0 16 16" fill="none" stroke="#fff" stroke-width="1.8"><path d="M4 12L12 4M6 4h6v6"/></svg></div>
</div>
<div class="abs do-card" style="left:617px;top:2882px">
  <div class="do-title">Employment Referrals</div>
  <p class="do-text" style="top:74px">Lorem ipsum dolor sit amet, consectetur adipiscing elit, sed do eiusmod tempor incididunt ut labore</p>
  <div class="arrow-btn"><svg width="16" height="16" viewBox="0 0 16 16" fill="none" stroke="#fff" stroke-width="1.8"><path d="M4 12L12 4M6 4h6v6"/></svg></div>
</div>

<div class="abs btn-orange" style="left:497px;top:3138px;width:206px;height:42px">VIEW MORE SERVICES</div>

<!-- testimonials -->
<h2 class="abs section-title" style="top:3368px">Customer Testimonials</h2>
<div class="abs testimonial">
  <div class="quote-mark">&ldquo;</div>
  <p class="testimonial-text">Lorem ipsum dolor sit amet, consectetur adipiscing elit, sed do eiusmod tempor incididunt ut labore et dolore magna aliqua. Ut enim ad minim veniam, quis nostrud exercitation ullamco.</p>
  <div class="testimonial-name">A.R., Southeast DC</div>
</div>
<svg class="abs" style="left:202px;top:3577px" width="16" height="20" viewBox="0 0 16 20" fill="none" stroke="var(--navy)" stroke-width="2"><path d="M12 2L4 10l8 8"/></svg>
<svg class="abs" style="left:974px;top:3577px" width="16" height="20" viewBox="0 0 16 20" fill="none" stroke="var(--navy)" stroke-width="2"><path d="M4 2l8 8-8 8"/></svg>

<!-- footer -->
<footer class="abs footer"></footer>
<div class="abs footer-brand">Novera Health</div>
<div class="abs footer-sub">SERVICES</div>

<div class="abs footer-heading" style="left:516px;top:3842px">Quick Links</div>
<div class="abs footer-link" style="left:516px;top:3908px">Home</div>
<div class="abs footer-link" style="left:516px;top:3944px">About Us</div>
<div class="abs footer-link" style="left:516px;top:3980px">Services</div>
<div class="abs footer-link" style="left:637px;top:3908px">Insurance</div>
<div class="abs footer-link" style="left:637px;top:3944px">FAQs</div>
<div class="abs footer-link" style="left:637px;top:3980px">Contact</div>

<div class="abs footer-heading" style="left:849px;top:3842px">Other Links</div>
<div class="abs footer-link" style="left:849px;top:3908px">Terms of Use</div>
<div class="abs footer-link" style="left:849px;top:3944px">Privacy Policy</div>
<div class="abs footer-link" style="left:849px;top:3980px">Sitemap</div>
<div class="abs footer-link" style="left:990px;top:3908px">Cookies</div>
<div class="abs footer-link" style="left:990px;top:3944px">References</div>

<div class="abs copyright">COPYRIGHT © 2025 - <span>NOVERA HEALTH SERVICES</span>. ALL RIGHT RESERVED</div>
<div class="abs social" style="left:900px;top:4078px"></div>
<div class="abs social" style="left:934px;top:4078px"></div>
<div class="abs social" style="left:967px;top:4078px"></div>
<div class="abs social" style="left:1000px;top:4078px"></div>
<div class="abs social" style="left:1033px;top:4078px"></div>

</body>
</html>
```